Commercial painting company is looking for a creative website designer.

Hi, we just completed our logo project and now ready to launch our website. The project will be done on Squarespace platform. It will contain:
Page 1 HOME
Page 2 SERVICES
Page 3 PICTURES
The content will be written by us. I am not sure bout the pictures, I do not have any to provide. I can buy stock photos if needed.
We are commercial only painting company and have to appeal to commercial, industrial property mangers. We will need CALL, REQUEST FOR ESTIMATE buttons.
If possible to have a live picture on home page would be great. Thank you
Target Market(s)
Property Managers
Industry/Entity Type
Commercial Painting
Other font styles liked:
- Poppins

```html
<!DOCTYPE html>
<html lang="en">
<head>
<meta charset="utf-8">
<title>CoatCraft Works – Commercial Painting</title>
<link href="https://fonts.googleapis.com/css2?family=Poppins:wght@400;500;700&display=swap" rel="stylesheet">
<style>
:root{
  --sky:#d3e8fb;
  --navy:#06206b;
  --ink:#000;
  --white:#fff;
  --blue-link:#2f80ed;
  --footer:#2b2b2b;
  --footer-bar:#0d0d0d;
  --footer-text:#e6e6e6;
  --line:#555;
}
*{box-sizing:border-box;margin:0;padding:0}
html,body{width:1200px;height:2788px;overflow:hidden}
body{font-family:'Poppins',sans-serif;color:var(--ink);background:var(--white);position:relative}
.abs{position:absolute}

/* hero */
.hero{left:0;top:0;width:1200px;height:1183px;background:var(--sky)}
.hero-navy{left:893px;top:0;width:307px;height:440px;background:var(--navy)}
.hero-arch{left:893px;top:255px;width:307px;height:480px;background:var(--sky);border-radius:160px 160px 0 0}
.brand{left:63px;top:50px;display:flex;align-items:center;gap:10px;font-weight:700;font-size:20px;color:var(--navy)}
.brand-dot{width:40px;height:40px;border-radius:50%;background:var(--navy)}
.nav{left:478px;top:62px;display:flex;gap:32px;font-size:19px}
.btn{display:flex;align-items:center;justify-content:center;border-radius:28px;font-size:19px;height:56px;border:1.5px solid var(--ink);color:var(--ink);background:transparent}
.btn-dark{background:var(--ink);color:var(--white)}
.btn-light{border-color:var(--white);color:var(--white)}
.nav-cta{left:949px;top:47px;width:187px}
.hero-title{left:62px;top:212px;font-size:70px;line-height:74px;font-weight:400;letter-spacing:1px}
.hero-text{left:64px;top:446px;width:470px;font-size:11.5px;line-height:17px}
.hero-pricing{left:62px;top:521px;width:189px}
.hero-more{left:252px;top:521px;width:189px}

.details{left:604px;top:309px;width:288px;height:365px;background:var(--white);border-radius:90px 0 80px 0;overflow:hidden}
.details-photo{left:0;top:0;width:92px;height:365px;background:linear-gradient(180deg,#111 0%,#2a1a2a 20%,#e24b7d 35%,#f0a13a 45%,#5fbf5a 55%,#2b7bd6 68%,#5a3bb0 80%,#1a1a2a 100%)}
.details-label{left:98px;top:10px;font-weight:700;font-size:17px}
.details-icon{left:250px;top:12px}
.details-name{left:98px;top:226px;font-size:18px;line-height:27px}
.details-band{left:92px;top:284px;width:196px;height:81px;background:linear-gradient(180deg,#f05a7e,#f7c948 30%,#7bd36f 50%,#50a8f0 72%,#a06ff0)}

.portal{left:923px;top:292px;width:244px;height:244px;border-radius:50%;background:radial-gradient(circle at 50% 45%,#ff7ab0 0%,#e9285f 30%,#8a2a8c 65%,#2f7fa8 100%);box-shadow:0 10px 24px rgba(0,0,0,.2)}
.swatch{border-radius:50%;border:4px solid var(--white)}

/* about */
.deco-left{left:0;top:670px;width:332px;height:552px;background:linear-gradient(160deg,#d9a0bf 0%,#7fb5dc 50%,#4d6f8c 100%);opacity:.55}
.card{background:var(--white);border-radius:70px 0 70px 0;box-shadow:0 8px 24px rgba(0,0,0,.06)}
.about{left:332px;top:737px;width:804px;height:374px}
.section-title{font-weight:700;font-size:31px;letter-spacing:.3px}
.about-title{left:70px;top:46px}
.about-text{left:70px;top:109px;width:657px;font-size:11.5px;line-height:17px;text-align:justify}
.about-more{left:70px;top:279px;width:189px}

/* services */
.services-title{left:63px;top:1275px;font-size:30px}
.service{top:1345px;width:530px;height:271px;background:var(--white);box-shadow:0 4px 18px rgba(0,0,0,.08);display:flex}
.service-photo{width:250px;height:271px;flex:none}
.service-body{padding:42px 22px 0 28px}
.service-name{font-weight:700;font-size:15px;margin-bottom:6px}
.service-text{font-size:11.5px;line-height:17px;text-align:justify}
.service-link{display:block;margin-top:8px;color:var(--blue-link);font-size:15px}

/* contact */
.contact-band{left:0;top:1749px;width:1200px;height:664px;background:var(--sky)}
.deco-right{left:869px;top:1677px;width:331px;height:552px;background:linear-gradient(340deg,#d9a0bf 0%,#7fb5dc 50%,#4d6f8c 100%);opacity:.55}
.contact{left:63px;top:1791px;width:804px;height:546px}
.contact-title{left:74px;top:63px}
.field{border:1px solid #333;background:var(--white);font-size:11px;color:#888;padding:0 24px;display:flex;align-items:center;height:31px}
.field-select{justify-content:space-between}
.field-area{align-items:flex-start;padding-top:13px}
.send{left:70px;top:430px;width:138px}

/* footer */
.footer{left:0;top:2413px;width:1200px;height:343px;background:var(--footer);color:var(--footer-text)}
.footer-bar{left:0;top:2756px;width:1200px;height:32px;background:var(--footer-bar);color:var(--footer-text);font-size:10px;display:flex;align-items:center;justify-content:center}
.footer-brand{left:133px;top:80px;width:297px;display:flex;align-items:center;justify-content:center;gap:10px;font-weight:700;font-size:19px;color:var(--white)}
.footer-brand .brand-dot{background:#c8313e}
.footer-about{left:133px;top:170px;width:297px;font-size:11.5px;line-height:17px;text-align:justify}
.footer-divider{left:491px;top:40px;width:1px;height:263px;background:var(--line)}
.footer-head{font-weight:700;font-size:11px;color:var(--white)}
.footer-list{font-size:11px;line-height:14px}
.contact-item{display:flex;gap:8px;margin-bottom:14px}
.contact-item b{font-weight:700;color:var(--white)}
.social{display:flex;gap:8px;margin-top:10px}
.social span{width:14px;height:14px;border-radius:50%;border:2px solid var(--footer-text)}
</style>
</head>
<body>

<section class="abs hero" aria-label="Hero">
  <div class="abs hero-navy"></div>
  <div class="abs hero-arch"></div>

  <div class="abs brand"><span class="brand-dot"></span>CoatCraft Works</div>
  <nav class="abs nav"><span>Home</span><span>Services</span><span>Gallery</span></nav>
  <a class="abs btn btn-light nav-cta">Get Pricing</a>

  <h1 class="abs hero-title">THE WORLD<br>BECOME<br>COLOR FULL</h1>
  <p class="abs hero-text">Lorem Ipsum is simply dummy text of the printing and typesetting industry. Lorem Ipsum has been the industry's standard dummy text ever since the 1500s,</p>
  <a class="abs btn btn-dark hero-pricing">Get Pricing</a>
  <a class="abs btn hero-more">Learn More</a>

  <div class="abs details">
    <div class="abs details-photo" role="img" aria-label="Close-up photo of rainbow coloured pigment powder"></div>
    <div class="abs details-label">DETAILS</div>
    <svg class="abs details-icon" width="30" height="30" viewBox="0 0 30 30"><circle cx="15" cy="15" r="14" fill="#000"/><path d="M10 20 L20 10 M12 10 H20 V18" stroke="#fff" stroke-width="2" fill="none"/></svg>
    <div class="abs details-name">COLOR CODE<br>STUDIO</div>
    <div class="abs details-band"></div>
  </div>

  <div class="abs portal" role="img" aria-label="Photo of a corridor lit in neon pink and red"></div>
  <div class="abs swatch" style="left:946px;top:594px;width:82px;height:82px;background:#fdbd5e"></div>
  <div class="abs swatch" style="left:993px;top:566px;width:102px;height:102px;background:#f0413a"></div>
  <div class="abs swatch" style="left:1060px;top:591px;width:84px;height:84px;background:var(--navy)"></div>

  <div class="abs deco-left" role="img" aria-label="Decorative artwork of layered coloured diamond frames"></div>

  <article class="abs card about">
    <h2 class="abs section-title about-title">ABOUT</h2>
    <p class="abs about-text">Lorem Ipsum is simply dummy text of the printing and typesetting industry. Lorem Ipsum has been the industry's standard dummy text ever since the 1500s, when an unknown printer took a galley of type and scrambled it to make a type specimen book. It has survived not only five centuries, but also the leap into electronic typesetting, remaining essentially unchanged. It was popularised in the 1960s with the release of Typeset sheets containing Lorem Ipsum passages, and more recently with desktop publishing software like Quill PageSetter including versions of Lorem Ipsum. Lorem Ipsum is simply dummy text of the printing and typesetting industry. Lorem Ipsum has been the industry's standard dummy text ever since the 1500s, when an unknown printer took a galley of type and scrambled it to make a type</p>
    <a class="abs btn about-more">Learn More</a>
  </article>
</section>

<section aria-label="Services">
  <h2 class="abs section-title services-title">OUR PAINTING SERVICES</h2>
  <article class="abs service" style="left:63px">
    <div class="service-photo" role="img" aria-label="Photo of two painters in blue aprons by an orange wall" style="background:linear-gradient(135deg,#e67a1f 0%,#f0a050 45%,#2d4fa8 70%,#1e2f6a 100%)"></div>
    <div class="service-body">
      <h3 class="service-name">COMMERCIAL PAINTING</h3>
      <p class="service-text">It is a long established fact that a reader will be distracted by the readable content of a page when looking at its layout. The point of using Lorem Ipsum is that it has a more-or-less normal distribution of letters, as opposed to using 'Content here, content here', making it look like readable English.</p>
      <a class="service-link">READ MORE</a>
    </div>
  </article>
  <article class="abs service" style="left:606px">
    <div class="service-photo" role="img" aria-label="Photo of a paint roller covering a dark wall in white" style="background:linear-gradient(90deg,#1a1f24 0%,#2b3238 35%,#c9d3da 60%,#eef2f5 100%)"></div>
    <div class="service-body">
      <h3 class="service-name">RESTORE PAINTING</h3>
      <p class="service-text">It is a long established fact that a reader will be distracted by the readable content of a page when looking at its layout. The point of using Lorem Ipsum is that it has a more-or-less normal distribution of letters, as opposed to using 'Content here, content here', making it look like readable English.</p>
      <a class="service-link">READ MORE</a>
    </div>
  </article>
</section>

<section aria-label="Contact">
  <div class="abs contact-band"></div>
  <div class="abs deco-right" role="img" aria-label="Decorative artwork of layered coloured diamond frames"></div>
  <form class="abs card contact">
    <h2 class="abs section-title contact-title">CONTACT US</h2>
    <div class="abs field" style="left:70px;top:130px;width:325px">First Name</div>
    <div class="abs field" style="left:409px;top:130px;width:325px">Last Name</div>
    <div class="abs field" style="left:70px;top:173px;width:325px">Email Address</div>
    <div class="abs field" style="left:409px;top:173px;width:325px">Phone No.</div>
    <div class="abs field field-select" style="left:70px;top:216px;width:664px">Please select the service
      <svg width="12" height="8" viewBox="0 0 12 8"><path d="M1 1 L6 6 L11 1" stroke="#000" stroke-width="2" fill="none"/></svg>
    </div>
    <div class="abs field field-area" style="left:70px;top:260px;width:664px;height:156px">Message ...</div>
    <a class="abs btn btn-dark send">Send</a>
  </form>
</section>

<footer>
  <div class="abs footer">
    <div class="abs footer-brand"><span class="brand-dot"></span>CoatCraft Works</div>
    <p class="abs footer-about">It is a long established fact that a reader will be distracted by the readable content of a page when looking at its layout. The point of using Lorem Ipsum is that it has a more-or-less normal distribution of letters, as opposed to using 'Content here, content here', making it look like readable English.</p>
    <div class="abs footer-divider"></div>

    <div class="abs" style="left:553px;top:80px;width:200px">
      <div class="footer-head" style="margin-bottom:22px">CONTACT US</div>
      <div class="footer-list">
        <div class="contact-item">
          <svg width="16" height="16" viewBox="0 0 16 16"><path d="M15 1 L1 7 L7 9 L9 15 Z" fill="#e6e6e6"/></svg>
          <span>Elm Street, Springfield,<br>ST 00000</span>
        </div>
        <div class="contact-item">
          <svg width="16" height="12" viewBox="0 0 16 12"><rect x="0" y="0" width="16" height="12" rx="1" fill="#e6e6e6"/><path d="M1 1 L8 7 L15 1" stroke="#2b2b2b" stroke-width="1.5" fill="none"/></svg>
          <span><b>Email:</b><br>info@coatcraftworks.com</span>
        </div>
        <div class="contact-item">
          <svg width="16" height="16" viewBox="0 0 16 16"><path d="M3 1 L6 1 L7 5 L5 6.5 C6 9 7 10 9.5 11 L11 9 L15 10 L15 13 C15 14 14 15 13 15 C6 15 1 10 1 3 C1 2 2 1 3 1 Z" fill="#e6e6e6"/></svg>
          <span><b>Phone No:</b><br>+1 (555) 010-2468</span>
        </div>
      </div>
    </div>

    <div class="abs" style="left:777px;top:80px">
      <div class="footer-head" style="margin-bottom:30px">CONTACT US</div>
      <div class="footer-list" style="line-height:31px">HOME<br>SERVICES<br>GALLERY</div>
    </div>

    <div class="abs" style="left:956px;top:80px">
      <div class="footer-head" style="margin-bottom:30px">OTHER LINKS</div>
      <div class="footer-list" style="line-height:31px">Privacy Policy<br>Terms &amp; Conditions<br>FAQ's</div>
      <div class="footer-head" style="margin-top:26px">OTHER LINKS</div>
      <div class="social"><span></span><span></span></div>
    </div>
  </div>
  <div class="abs footer-bar"><b>CoatCraft Works © 2023.</b>&nbsp;All rights reserved.</div>
</footer>

</body>
</html>
```